Compatible Printer Cartridge Box Design

We are looking to package toners cartridges & ink cartridges that we recycle in our shop. Attached is a doc file that tell what design we want, ideas, and sizes.

Unlike other compatible toner cartridges that are manufactured from scratch, LUMO Print Consumables are made from recycled original OEM print toners. This will maintain the original OEM parts inside the cartridge, maintain the original cartridge tolerance, ensure proper cartridge alignment in the printer, and minimize human error.

Project Deadline Extended
Reason: Hi to all, I am not satisfied with the current designs. I will extend for more 5 days and increase the budget. Thank You

Target Market(s)

Construction Companies, Banks, Hospitals, Oil Companies, Insurance Companies

Industry/Entity Type

Printer

Font styles to use
Other font styles liked:
• Calibri

Requirements
Must have
• The file must be in .ai format. So we can change the size of the box any time later.
• The file must be ready to be given to the printing press (specially the die cut). No any alteration must be made from our side.
• Since there are different models of cartridges, one side of the box must be left for a label that state the cartridge model, bar code, and compatible printers.
• The theme of the box must be quoted from our company logo, specially the colors. We prefer bold corporate design. Maybe with a woman on it (Not a must), and something related to protecting the environment. Avoid using the carton brown color.
• We prefer toner box that Can be opened from the top with that cartoon lock. For the ink cartridge, we would like to look like the zx one.
Nice to have
• Maybe with a woman on it (Not a must), and something related to protecting the environment.
Should not have
• Avoid using the carton brown color.

```html
<!DOCTYPE html>
<html lang="en">
<head>
<meta charset="utf-8">
<title>LUMO Premium Toner – Box Panels</title>
<link rel="stylesheet" href="https://fonts.googleapis.com/css2?family=Carlito:wght@400;700&family=Russo+One&display=swap">
<style>
  :root {
    --canvas-bg: #eef0ea;
    --panel-white: #f3f4f4;
    --leaf-green: #86a83a;
    --leaf-green-dark: #6f9130;
    --sun-yellow: #f3e23a;
    --pale-yellow: #f5f09a;
    --toner-orange: #f0a22a;
    --ink: #1f1f1f;
    --ink-soft: #3b3b3b;
    --panel-edge: #d6d8d2;
  }
  * { margin: 0; padding: 0; box-sizing: border-box; }
  html, body { width: 1200px; height: 1200px; overflow: hidden; }
  body {
    background: var(--canvas-bg);
    font-family: "Carlito", "Calibri", sans-serif;
    position: relative;
  }
  .box-net { position: absolute; left: 70px; top: 290px; width: 1060px; height: 620px; }
  .panel { position: absolute; overflow: hidden; background: var(--panel-white); box-shadow: 0 0 0 1px var(--panel-edge); }
  .panel svg.art { position: absolute; inset: 0; width: 100%; height: 100%; }

  .panel--top   { left: 0; top: 0; width: 760px; height: 200px; }
  .panel--front { left: 0; top: 200px; width: 760px; height: 420px; }
  .panel--end   { left: 760px; top: 200px; width: 300px; height: 420px; }

  .brand-mark { position: absolute; display: flex; flex-direction: column; align-items: center; gap: 4px; }
  .brand-mark__square { width: 46px; height: 46px; background: var(--toner-orange); }
  .brand-mark__name { font-weight: 700; font-size: 17px; color: var(--leaf-green-dark); }

  .product-title {
    position: absolute;
    font-family: "Russo One", sans-serif;
    font-weight: 400;
    line-height: 1;
    color: var(--ink);
    letter-spacing: 0.5px;
    white-space: nowrap;
  }
  .product-title--front { left: 88px; top: 36px; font-size: 50px; }
  .product-title--top   { left: 112px; top: 62px; font-size: 46px; }

  .product-tagline {
    position: absolute;
    font-weight: 700;
    color: var(--ink-soft);
    white-space: nowrap;
  }
  .product-tagline--front { left: 520px; top: 96px; font-size: 26px; }
  .product-tagline--top   { left: 450px; top: 114px; font-size: 22px; }

  .benefit-list { position: absolute; left: 22px; top: 122px; list-style: none; display: flex; flex-direction: column; gap: 7px; }
  .benefit-list li {
    background: var(--pale-yellow);
    color: var(--ink-soft);
    font-weight: 700;
    font-size: 15px;
    padding: 3px 10px;
    border-radius: 5px;
    width: fit-content;
  }

  .company-info {
    position: absolute; left: 28px; top: 236px; width: 244px;
    background: rgba(245, 240, 154, 0.92);
    border-radius: 10px;
    padding: 10px 14px;
    color: var(--ink-soft);
    font-style: normal;
    font-size: 14px; line-height: 1.22;
  }
  .company-info h3 { font-size: 17px; font-weight: 700; margin-bottom: 3px; color: var(--ink); }

  .top-flip { position: absolute; inset: 0; transform: rotate(180deg); }

  .soft-fill { position: absolute; border-radius: 50%; }
</style>
</head>
<body>
<main class="box-net">

  <section class="panel panel--top" aria-label="Top panel">
    <svg class="art" viewBox="0 0 760 200" preserveAspectRatio="none">
      <path d="M0 60 C200 20 420 150 760 110 L760 200 L0 200 Z" fill="var(--sun-yellow)"/>
      <path d="M0 95 C220 55 430 185 760 150 L760 200 L0 200 Z" fill="var(--toner-orange)"/>
    </svg>
    <div class="top-flip">
      <div class="brand-mark" style="right:20px; top:12px;">
        <span class="brand-mark__square"></span>
        <span class="brand-mark__name">Nerida</span>
      </div>
      <div class="product-title product-title--top">LUMO Premium Toner</div>
      <div class="product-tagline product-tagline--top">Printing Happy</div>
    </div>
  </section>

  <section class="panel panel--front" aria-label="Front panel">
    <svg class="art" viewBox="0 0 760 420" preserveAspectRatio="none">
      <rect x="0" y="150" width="760" height="270" fill="var(--leaf-green)"/>
      <path d="M0 360 C180 340 300 200 440 150 C560 110 660 100 760 95 L760 230 C640 240 540 260 430 300 C300 350 160 390 0 400 Z" fill="var(--sun-yellow)"/>
      <path d="M60 395 C220 380 330 270 460 215 C580 170 680 160 760 160 L760 260 C640 265 540 300 440 340 C330 385 200 410 60 415 Z" fill="var(--toner-orange)"/>
      <path d="M0 400 C160 390 300 350 430 300 C540 260 640 240 760 230 L760 420 L0 420 Z" fill="var(--leaf-green)"/>
    </svg>
    <div class="soft-fill" role="img" aria-label="Soft halftone dot pattern and white paint splash across the orange wave"
         style="left:250px; top:170px; width:300px; height:150px;
                background: radial-gradient(ellipse at center, rgba(255,255,255,0.55), rgba(255,255,255,0) 70%);"></div>
    <div class="soft-fill" role="img" aria-label="White leaf outline decoration"
         style="left:430px; top:320px; width:90px; height:80px;
                background: radial-gradient(ellipse at center, rgba(255,255,255,0.5), rgba(255,255,255,0) 70%);"></div>

    <div class="brand-mark" style="left:20px; top:14px;">
      <span class="brand-mark__square"></span>
      <span class="brand-mark__name">Nerida</span>
    </div>
    <h1 class="product-title product-title--front">LUMO Premium Toner</h1>
    <p class="product-tagline product-tagline--front">Printing Happy</p>

    <ul class="benefit-list">
      <li>Save up to 70% of your printing expenses</li>
      <li>Recycle Today for Better Tomorrow</li>
      <li>Environment Friendly Solution</li>
    </ul>
  </section>

  <section class="panel panel--end" aria-label="End panel">
    <svg class="art" viewBox="0 0 300 420" preserveAspectRatio="none">
      <rect x="0" y="215" width="300" height="205" fill="var(--leaf-green)"/>
    </svg>
    <div class="soft-fill" role="img" aria-label="Green leaf outline decoration"
         style="left:120px; top:40px; width:160px; height:150px;
                background: radial-gradient(ellipse at center, rgba(134,168,58,0.35), rgba(134,168,58,0) 70%);"></div>
    <div class="soft-fill" role="img" aria-label="Pale paint splash behind contact details"
         style="left:10px; top:225px; width:280px; height:180px;
                background: radial-gradient(ellipse at center, rgba(255,255,255,0.35), rgba(255,255,255,0) 70%);"></div>

    <div class="brand-mark" style="left:22px; top:30px;">
      <span class="brand-mark__square"></span>
      <span class="brand-mark__name">Nerida</span>
    </div>

    <address class="company-info">
      <h3>Company Info:</h3>
      <p>Nerida Ink &amp; Printing Materials</p>
      <p>42 Harbour Lane</p>
      <p>Marin City, Westland</p>
      <p>PO Box: 40218</p>
      <p>Tel: +00 4 5550199</p>
      <p>ink@nerida.example</p>
      <p>www.nerida.example</p>
    </address>
  </section>

</main>
</body>
</html>
```